Billboard Velmarhof - Maison K

I need two Billboards (125cm width x 340 height) -. They will be standing side by side in front of a building. Each billboard contains details of a business. 1. Medical center: VELMARHOF DRONSEL 2. Beauty saloon/Permanent make-up. MAISON K & ZOW Clinic. We already have a mockup. (see uploads). We want a design fitting the building with upmarket look. Modern, fresh and classy. The billboards need to have the same background color as in the mockup: dark-grey/black. The medical center has a green accent and the Beauty salon soft pink. The billboards should have certain uniformity.

Target Market(s)

Upmarket men and women

Font styles to use
Sans Serif

Requirements
Must have
• WE LIKE OUT OF THE BOX DESIGNS

VELMARHOF DRONSEL
Uw rug is onze zorg - this is the tagline
hello@velmarhofdronsel.be
09 614 28 90
www.velmarhofdronsel.be
facebook icon | instagram icon

MAISON K (HAS TWO DEPARTMENTS)
1. Schoonheidsinstituut - (which means beauty salon)
2. ZOW clinic (which means permanent make up)
0486 91 37 52
hello@maisonk.be
www.maisonk.be

hello@maisonk.be
Should not have
• not curly, not kitch, no color-books
NO PICTURES IN DESIGN

```html
<!DOCTYPE html>
<html lang="nl">
<head>
<meta charset="utf-8">
<title>Billboards Velmarhof Dronsel – Maison K</title>
<link rel="stylesheet" href="https://fonts.googleapis.com/css2?family=Montserrat:wght@300;400;600&family=Oswald:wght@300&display=swap">
<style>
  :root {
    --canvas: #e4e4e4;
    --panel: #363636;
    --white: #ffffff;
    --green: #8cc63f;
    --pink: #ffcaca;
    --ink: #2e2e2e;
    --rule-pink: #e8b4b4;
  }
  * { margin: 0; padding: 0; box-sizing: border-box; }
  html, body {
    width: 1200px; height: 1200px; overflow: hidden;
    background: var(--canvas);
  }
  .stage { position: relative; width: 1200px; height: 1200px; }
  .billboard {
    position: absolute; top: 98px; width: 369px; height: 1003px;
    box-shadow: 0 6px 18px rgba(0,0,0,0.18);
  }
  .billboard--medical { left: 158px; }
  .billboard--beauty { left: 674px; }
  .billboard svg { display: block; width: 100%; height: 100%; }

  .panel { fill: var(--panel); }
  .fill-white { fill: var(--white); }
  .fill-green { fill: var(--green); }
  .fill-pink { fill: var(--pink); }
  .fill-panel { fill: var(--panel); }

  .brand-name {
    font-family: 'Montserrat', sans-serif; font-weight: 600;
    fill: var(--white); letter-spacing: 4px;
  }
  .tagline {
    font-family: 'Montserrat', sans-serif; font-weight: 300;
    font-size: 92px;
  }
  .tagline--white { fill: var(--white); }
  .tagline--green { fill: var(--green); }
  .contact {
    font-family: 'Montserrat', sans-serif; font-weight: 300;
    font-size: 31px; fill: var(--white); text-anchor: middle;
  }
  .contact--small { font-size: 27px; }
  .accent-green { fill: var(--green); }
  .accent-pink { fill: var(--pink); }
  .rule-green { stroke: var(--green); stroke-width: 1.6; }
  .rule-pink { stroke: var(--rule-pink); stroke-width: 1.6; }
  .icon-green { fill: none; stroke: var(--green); stroke-width: 2; stroke-linejoin: round; stroke-linecap: round; }
  .icon-pink { fill: none; stroke: var(--rule-pink); stroke-width: 2; stroke-linejoin: round; stroke-linecap: round; }

  .salon-name {
    font-family: 'Montserrat', sans-serif; font-weight: 400;
    font-size: 52px; fill: var(--white); text-anchor: middle;
  }
  .clinic-name {
    font-family: 'Montserrat', sans-serif; font-weight: 400;
    font-size: 50px; fill: var(--white); text-anchor: middle;
  }
  .clinic-sub {
    font-family: 'Montserrat', sans-serif; font-weight: 400;
    font-size: 16px; fill: var(--white); letter-spacing: 4px; text-anchor: middle;
  }
  .label {
    font-family: 'Oswald', sans-serif; font-weight: 300;
    font-size: 58px; fill: var(--ink); text-anchor: middle;
  }
  .social-dot-green { fill: none; stroke: var(--green); stroke-width: 3; }
  .social-dot-pink { fill: none; stroke: #d89a9a; stroke-width: 3; }
</style>
</head>
<body>
<main class="stage">

  <!-- Medical centre billboard -->
  <section class="billboard billboard--medical" aria-label="Velmarhof Dronsel">
    <svg viewBox="0 0 594 1616" xmlns="http://www.w3.org/2000/svg">
      <rect class="panel" width="594" height="1616"/>

      <g class="brand">
        <text class="brand-name" x="82" y="355" font-size="46">VELMARHOF</text>
        <text class="brand-name" x="82" y="405" font-size="40">DRONSEL</text>
      </g>

      <text class="tagline tagline--white" x="82" y="596">Uw rug is</text>
      <text class="tagline tagline--green" x="78" y="690">onze zorg</text>

      <g class="wave-top">
        <path class="fill-green" d="M0 830 Q170 960 340 860 Q470 780 594 790 L594 805 Q470 780 340 895 Q160 1010 0 870 Z"/>
        <path class="fill-white" d="M0 797 Q170 910 340 845 Q460 790 594 775 L594 790 Q460 790 340 860 Q170 950 0 812 Z"/>
        <path class="fill-white" d="M360 830 Q480 750 594 800 L594 885 Q490 770 360 830 Z"/>
      </g>

      <g class="contact-block">
        <line class="rule-green" x1="90" y1="1011" x2="265" y2="1011"/>
        <line class="rule-green" x1="329" y1="1011" x2="503" y2="1011"/>
        <g class="icon-green"><rect x="283" y="1002" width="28" height="19"/><path d="M283 1002 L297 1013 L311 1002"/></g>
        <text class="contact" x="297" y="1071">hello@velmarhofdronsel.be</text>

        <line class="rule-green" x1="90" y1="1113" x2="265" y2="1113"/>
        <line class="rule-green" x1="329" y1="1113" x2="503" y2="1113"/>
        <path class="icon-green" d="M286 1102 q-4 4 2 13 q7 10 16 11 l4 -5 l-6 -4 l-3 3 q-5 -2 -8 -8 l3 -3 l-4 -6 Z"/>
        <text class="contact" x="297" y="1173">09 614 28 90</text>

        <line class="rule-green" x1="90" y1="1206" x2="265" y2="1206"/>
        <line class="rule-green" x1="329" y1="1206" x2="503" y2="1206"/>
        <g class="icon-green"><path d="M308 1195 q-14 1 -20 16 l6 6 q15 -6 16 -20 Z"/><path d="M290 1214 l-6 8 M294 1218 l-4 6"/></g>
        <text class="contact" x="297" y="1275">www.<tspan class="accent-green">VelmarhofDronsel</tspan>.be</text>

        <line class="rule-green" x1="90" y1="1349" x2="503" y2="1349"/>
        <rect class="fill-white" x="201" y="1321" width="192" height="56" rx="28"/>
        <circle class="social-dot-green" cx="263" cy="1349" r="17"/>
        <circle class="social-dot-green" cx="332" cy="1349" r="17"/>
      </g>

      <g class="wave-bottom">
        <path class="fill-green" d="M0 1470 Q90 1540 240 1530 Q420 1500 594 1540 L594 1616 L0 1616 Z"/>
        <path class="fill-white" d="M0 1555 Q150 1625 320 1530 Q470 1420 594 1470 L594 1515 Q470 1440 320 1555 Q160 1665 0 1570 Z"/>
        <path class="fill-panel" d="M0 1565 Q160 1650 320 1548 Q470 1445 594 1505 L594 1512 Q470 1455 320 1556 Q160 1660 0 1572 Z"/>
      </g>
    </svg>
  </section>

  <!-- Beauty salon billboard -->
  <section class="billboard billboard--beauty" aria-label="Maison K en ZOW Clinic">
    <svg viewBox="0 0 594 1616" xmlns="http://www.w3.org/2000/svg">
      <rect class="panel" width="594" height="1616"/>

      <g class="brand">
        <circle cx="297" cy="160" r="52" fill="none" stroke="var(--white)" stroke-width="3"/>
        <text class="salon-name" x="297" y="310">Maison K</text>
      </g>

      <path class="fill-pink" d="M90 370 H513 Q533 370 533 390 V460 H90 Q60 460 60 430 V400 Q60 370 90 370 Z"/>
      <text class="label" x="297" y="436" textLength="400" lengthAdjust="spacingAndGlyphs">Schoonheidsinstituut</text>

      <g class="contact-block">
        <line class="rule-pink" x1="123" y1="494" x2="269" y2="494"/>
        <line class="rule-pink" x1="324" y1="494" x2="471" y2="494"/>
        <g class="icon-pink"><rect x="285" y="486" width="24" height="16"/><path d="M285 486 L297 495 L309 486"/></g>
        <text class="contact contact--small" x="297" y="540">hello@maisonk.be</text>

        <line class="rule-pink" x1="123" y1="572" x2="269" y2="572"/>
        <line class="rule-pink" x1="324" y1="572" x2="471" y2="572"/>
        <path class="icon-pink" d="M288 563 q-3 4 2 11 q6 9 14 10 l3 -4 l-5 -4 l-3 3 q-4 -2 -7 -7 l3 -3 l-3 -5 Z"/>
        <text class="contact contact--small" x="297" y="620">0486 91 37 52</text>

        <line class="rule-pink" x1="123" y1="644" x2="269" y2="644"/>
        <line class="rule-pink" x1="324" y1="644" x2="471" y2="644"/>
        <g class="icon-pink"><path d="M306 635 q-12 1 -17 14 l5 5 q13 -5 14 -17 Z"/><path d="M291 651 l-5 7"/></g>
        <text class="contact contact--small" x="297" y="699">www.<tspan class="accent-pink">MaisonK</tspan>.be</text>

        <line class="rule-pink" x1="123" y1="755" x2="471" y2="755"/>
        <rect class="fill-white" x="216" y="731" width="161" height="48" rx="24"/>
        <circle class="social-dot-pink" cx="268" cy="755" r="15"/>
        <circle class="social-dot-pink" cx="327" cy="755" r="15"/>
      </g>

      <g class="wave-top">
        <path class="fill-pink" d="M0 830 Q150 960 330 870 Q470 790 594 800 L594 810 Q470 800 330 895 Q150 1000 0 880 Z"/>
        <path class="fill-white" d="M0 805 Q160 905 340 850 Q460 800 594 785 L594 798 Q460 805 340 865 Q160 945 0 820 Z"/>
        <path class="fill-white" d="M360 840 Q480 760 594 810 L594 895 Q490 780 360 840 Z"/>
      </g>

      <g class="clinic">
        <text class="clinic-name" x="297" y="1010">ZOW Clinic</text>
        <text class="clinic-sub" x="297" y="1082">PERMANENT MAKE UP BY LOTTE VERHAEGEN</text>
      </g>

      <path class="fill-pink" d="M90 1108 H513 Q533 1108 533 1128 V1199 H90 Q60 1199 60 1169 V1138 Q60 1108 90 1108 Z"/>
      <text class="label" x="297" y="1175" textLength="390" lengthAdjust="spacingAndGlyphs">Permanent Make up</text>

      <g class="contact-block">
        <line class="rule-pink" x1="123" y1="1234" x2="269" y2="1234"/>
        <line class="rule-pink" x1="324" y1="1234" x2="471" y2="1234"/>
        <g class="icon-pink"><rect x="285" y="1226" width="24" height="16"/><path d="M285 1226 L297 1235 L309 1226"/></g>
        <text class="contact contact--small" x="297" y="1281">hello@zowclinic.be</text>

        <line class="rule-pink" x1="123" y1="1313" x2="269" y2="1313"/>
        <line class="rule-pink" x1="324" y1="1313" x2="471" y2="1313"/>
        <path class="icon-pink" d="M288 1304 q-3 4 2 11 q6 9 14 10 l3 -4 l-5 -4 l-3 3 q-4 -2 -7 -7 l3 -3 l-3 -5 Z"/>
        <text class="contact contact--small" x="297" y="1361">0486 91 37 52</text>

        <line class="rule-pink" x1="123" y1="1386" x2="269" y2="1386"/>
        <line class="rule-pink" x1="324" y1="1386" x2="471" y2="1386"/>
        <g class="icon-pink"><path d="M306 1377 q-12 1 -17 14 l5 5 q13 -5 14 -17 Z"/><path d="M291 1393 l-5 7"/></g>
        <text class="contact contact--small" x="297" y="1439">www.<tspan class="accent-pink">ZowClinic</tspan>.be</text>
      </g>

      <g class="wave-bottom">
        <path class="fill-pink" d="M0 1485 Q90 1555 240 1545 Q420 1515 594 1550 L594 1616 L0 1616 Z"/>
        <path class="fill-white" d="M0 1565 Q150 1630 320 1540 Q470 1430 594 1485 L594 1525 Q470 1455 320 1565 Q160 1670 0 1580 Z"/>
        <path class="fill-panel" d="M0 1575 Q160 1655 320 1558 Q470 1458 594 1515 L594 1522 Q470 1468 320 1566 Q160 1665 0 1582 Z"/>
      </g>
    </svg>
  </section>

</main>
</body>
</html>
```